design a catchy flyer for my electrical buisness

need a flyer designed to attract people to my business by looking professional and offering specials

Target Market(s)

all people i want to look affordable to everyone but still keeping that professional look and feel

Industry/Entity Type

Electrical

Requirements
Must have
• NO JOB TO BIG OR SMALL
• CALL NOW FOR A FREE QUOTE 0400318726
• NO CALL OUT FEE
• same promises as uploaded pic maybe written different style
• Your neighborhood electrician
• 100% satisfaction guaranteed
• were here to help
• mention this flyer for 10% off
• specializing in house renovations, extensions, kitchen and bathroom upgrades switchboard upgrades
• Make your house safe with our RCD and smoke alarm packages
Nice to have
• modern
• proffesional
• shows trust when customers read it
Should not have
• corny slogans
• cheap look

```html
<!DOCTYPE html>
<html lang="en">
<head>
<meta charset="utf-8">
<title>Your Neighborhood Electrician – VoltLane Flyer</title>
<link rel="stylesheet" href="https://fonts.googleapis.com/css2?family=Roboto+Condensed:wght@300;400;700;900&display=swap">
<style>
  :root{
    --page:#1f252c;
    --cream:#fff8b8;
    --gold:#ffc62a;
    --gold-deep:#ffb400;
    --red:#c8102e;
    --red-bright:#e3202a;
    --blue:#1d5fc0;
    --blue-deep:#12379a;
    --lemon:#fff200;
    --orange:#f07c1a;
    --grey:#8a8a8a;
    --ink:#1b1b1b;
    --white:#ffffff;
  }
  *{margin:0;padding:0;box-sizing:border-box}
  html,body{width:1200px;height:1200px;overflow:hidden;background:var(--page)}
  body{font-family:"Roboto Condensed",Arial,sans-serif;position:relative}

  .flyer{position:absolute;left:230px;top:30px;width:740px;height:1140px;background:var(--cream);overflow:hidden}
  .flyer > *{position:absolute}

  .edge-strip{left:0;top:0;width:28px;height:800px;background:linear-gradient(var(--gold) 0%,var(--gold) 30%,var(--cream) 100%)}
  .gold-column{left:490px;top:0;width:250px;height:520px;background:linear-gradient(var(--gold),var(--gold-deep))}
  .blue-column{left:480px;top:210px;width:240px;height:910px;background:linear-gradient(var(--blue-deep) 0%,var(--blue) 55%,#1a7fd0 100%)}

  .tagline{left:65px;top:112px;font-size:30px;font-weight:700;color:var(--grey)}

  .title-band{left:0;top:165px;width:540px;height:248px;background:linear-gradient(90deg,var(--red),var(--red-bright))}
  .title-small{left:42px;top:182px;font-size:54px;font-weight:400;color:var(--white);letter-spacing:-0.5px}
  .title-large{left:36px;top:262px;font-size:100px;font-weight:900;color:var(--white);letter-spacing:-1px;line-height:1}

  .photo{left:470px;top:150px;width:270px;height:440px;background:linear-gradient(170deg,#e9e2cf 0%,#5a6fd0 35%,#2f46b5 70%,#8f9bb0 100%);border-radius:6px}

  .promise-head{left:52px;top:428px;font-size:31px;font-weight:700;color:var(--orange)}
  .promises{left:50px;top:474px;width:420px;list-style:none}
  .promises li{position:relative;padding-left:24px;font-size:18px;line-height:1.2;color:var(--ink);margin-bottom:8px}
  .promises svg{position:absolute;left:0;top:3px;width:14px;height:14px}

  .specials{left:0;top:800px;width:480px;height:155px;background:var(--lemon);padding:20px 24px 0 50px}
  .specials ul{list-style:none}
  .specials li{position:relative;font-size:19px;line-height:1.2;color:var(--ink);margin-bottom:12px}
  .specials li::before{content:"";position:absolute;left:-24px;top:8px;width:7px;height:7px;border-radius:50%;background:var(--ink)}

  .footer{left:0;top:955px;width:480px;height:185px;background:var(--white)}
  .footer svg{position:absolute;left:0;top:0}
  .brand{left:135px;top:1000px;display:flex;align-items:center;gap:14px}
  .brand-dot{width:44px;height:44px;border-radius:50%;border:4px solid var(--orange)}
  .brand-name{font-size:36px;font-weight:400;color:var(--orange)}
  .brand-phone{left:128px;top:1062px;font-size:36px;font-weight:700;color:var(--orange);letter-spacing:1px}

  .badge{left:490px;top:570px;width:220px;height:220px}
  .badge-text{left:490px;top:612px;width:220px;text-align:center;color:var(--white);font-weight:900;line-height:1}
  .badge-text .big{font-size:54px;display:block}
  .badge-text .small{font-size:27px;font-weight:700;display:block;margin-top:6px;line-height:1.15}

  .call{left:480px;top:810px;width:240px;text-align:center;line-height:1.05}
  .call .call-line{display:block;font-size:34px;font-weight:300;color:var(--white)}
  .call .free{display:block;font-size:34px;font-weight:400;color:var(--red-bright)}
  .call .phone{display:block;font-size:32px;font-weight:900;color:var(--ink);margin-top:6px;white-space:nowrap}

  .discount{left:490px;top:975px;width:220px;height:150px}
  .discount-text{left:490px;top:1024px;width:220px;text-align:center;color:var(--white);font-size:48px;line-height:1}
  .discount-text b{font-weight:900}
  .discount-text span{font-weight:400}
</style>
</head>
<body>
<main class="flyer">
  <div class="edge-strip"></div>
  <div class="gold-column"></div>
  <div class="blue-column"></div>

  <p class="tagline">were here to help</p>

  <div class="title-band"></div>
  <div class="photo" role="img" aria-label="Photo of a smiling electrician in blue overalls carrying a coil of cable, with a tool belt and multimeter"></div>
  <h1 class="title-small">Your Neighborhood</h1>
  <p class="title-large">Electrician</p>

  <h2 class="promise-head">NO JOB TO BIG OR SMALL</h2>
  <ul class="promises">
    <li><svg viewBox="0 0 16 16"><path d="M2 9l4 4 8-10" fill="none" stroke="#555" stroke-width="3"/></svg>We will provide you with a fixed price<br>gurantee assuring no extra costs</li>
    <li><svg viewBox="0 0 16 16"><path d="M2 9l4 4 8-10" fill="none" stroke="#555" stroke-width="3"/></svg>We will leave your place as clean as when we arrived</li>
    <li><svg viewBox="0 0 16 16"><path d="M2 9l4 4 8-10" fill="none" stroke="#555" stroke-width="3"/></svg>We will rovide a 12 Month warranty on all parts</li>
    <li><svg viewBox="0 0 16 16"><path d="M2 9l4 4 8-10" fill="none" stroke="#555" stroke-width="3"/></svg>We will provide friendly, helpful service and advice</li>
    <li><svg viewBox="0 0 16 16"><path d="M2 9l4 4 8-10" fill="none" stroke="#555" stroke-width="3"/></svg>We will arrive on time or we will pay you $100</li>
    <li><svg viewBox="0 0 16 16"><path d="M2 9l4 4 8-10" fill="none" stroke="#555" stroke-width="3"/></svg>Before any job begins you will know the exat cost</li>
    <li><svg viewBox="0 0 16 16"><path d="M2 9l4 4 8-10" fill="none" stroke="#555" stroke-width="3"/></svg>If there is a problem and it’s our fault<br>we will fix it for free</li>
    <li><svg viewBox="0 0 16 16"><path d="M2 9l4 4 8-10" fill="none" stroke="#555" stroke-width="3"/></svg>We will return your telephone calls promptly</li>
    <li><svg viewBox="0 0 16 16"><path d="M2 9l4 4 8-10" fill="none" stroke="#555" stroke-width="3"/></svg>No Call Out Fee</li>
  </ul>

  <section class="specials">
    <ul>
      <li>Specializing in house renovations, extensions, kitchen and bathroom upgrades, Switchboard upgrades.</li>
      <li>Make your house safe with our <b>RCD and smoke alarm packages.</b></li>
    </ul>
  </section>

  <div class="footer">
    <svg width="480" height="185" viewBox="0 0 480 185">
      <path d="M40 0 H480 V160 C400 30 240 10 40 130 Z" fill="#fff8b8"/>
    </svg>
  </div>
  <div class="brand"><span class="brand-dot"></span><span class="brand-name">VoltLane</span></div>
  <p class="brand-phone">0400 318 726</p>

  <svg class="badge" viewBox="0 0 200 200">
    <g fill="#d41a2b">
      <rect x="30" y="30" width="140" height="140"/>
      <rect x="30" y="30" width="140" height="140" transform="rotate(18 100 100)"/>
      <rect x="30" y="30" width="140" height="140" transform="rotate(36 100 100)"/>
      <rect x="30" y="30" width="140" height="140" transform="rotate(54 100 100)"/>
      <rect x="30" y="30" width="140" height="140" transform="rotate(72 100 100)"/>
    </g>
  </svg>
  <p class="badge-text"><span class="big">100%</span><span class="small">satisfaction<br>guaranteed</span></p>

  <p class="call">
    <span class="call-line">CALL NOW</span>
    <span class="call-line">FOR A</span>
    <span class="free">FREE QUOTE</span>
    <span class="phone">0400 318 726</span>
  </p>

  <svg class="discount" viewBox="0 0 220 150">
    <ellipse cx="110" cy="75" rx="100" ry="66" fill="#1b6cc4"/>
    <path d="M45 130 C-8 90 22 20 118 10 C160 8 186 18 202 30" fill="none" stroke="#fff" stroke-width="4"/>
    <path d="M208 55 C222 110 160 145 86 140" fill="none" stroke="#fff" stroke-width="4"/>
  </svg>
  <p class="discount-text"><b>10%</b> <span>off</span></p>
</main>
</body>
</html>
```